Morvell Electric Business Card

An electrical contractor needs a business card design, that will stand out.
I would like designs that use the colors in the logo shown. The logo attached I am ok with but if you have a better idea I am open for suggestions. I like the color scheme.
Industry/Entity Type
Electrical
Contact Information for Business Card
Services, social media, QR code,

```html
<!DOCTYPE html>
<html lang="en">
<head>
<meta charset="utf-8">
<title>Morvell Electric Business Card</title>
<link rel="stylesheet" href="https://fonts.googleapis.com/css2?family=Montserrat:wght@600;700&family=Arimo:wght@400&display=swap">
<style>
  :root {
    --page-bg: #2b2b2b;
    --card-black: #0a0a0a;
    --card-red: #e30000;
    --accent-red: #e30613;
    --emboss-red: #f50a0a;
    --text-white: #ffffff;
  }
  * { box-sizing: border-box; margin: 0; padding: 0; }
  html, body { width: 1200px; height: 1015px; overflow: hidden; }
  body {
    background: var(--page-bg);
    display: flex;
    flex-direction: column;
    align-items: center;
    justify-content: center;
    gap: 60px;
  }
  .card {
    width: 700px;
    height: 400px;
    position: relative;
    overflow: hidden;
    box-shadow: 0 12px 30px rgba(0,0,0,0.55);
  }
  /* Front */
  .card-front {
    background: var(--card-black);
    display: flex;
    align-items: center;
    justify-content: center;
    gap: 22px;
  }
  .brand-dot {
    width: 54px; height: 54px;
    border-radius: 50%;
    background: var(--accent-red);
  }
  .brand-name {
    font-family: "Montserrat", sans-serif;
    font-weight: 700;
    font-size: 44px;
    letter-spacing: 1px;
    color: var(--text-white);
    text-transform: uppercase;
  }
  /* Back */
  .card-back { background: var(--card-red); }
  .emboss-mark {
    position: absolute;
    right: 40px; top: 55px;
    width: 300px; height: 240px;
    display: flex;
    align-items: center;
    justify-content: center;
  }
  .emboss-ring {
    position: absolute; inset: 0;
    border-radius: 50%;
    border: 3px solid var(--emboss-red);
    box-shadow: inset 1px 1px 2px rgba(0,0,0,0.15);
  }
  .emboss-name {
    font-family: "Montserrat", sans-serif;
    font-weight: 700;
    font-size: 26px;
    color: var(--emboss-red);
    text-transform: uppercase;
    letter-spacing: 1px;
  }
  .contact {
    position: absolute;
    left: 60px; top: 90px;
    color: var(--text-white);
    font-family: "Arimo", sans-serif;
  }
  .person-name {
    font-family: "Montserrat", sans-serif;
    font-weight: 700;
    font-size: 26px;
    letter-spacing: 0.5px;
    text-transform: uppercase;
    line-height: 1.1;
  }
  .person-role { font-size: 18px; margin-top: 2px; }
  .address { font-size: 18px; line-height: 1.25; margin: 26px 0 0 30px; }
  .contact-list { list-style: none; margin: 26px 0 0 40px; font-size: 18px; line-height: 1.35; }
  .contact-list li { display: flex; align-items: center; gap: 8px; }
  .contact-list svg { width: 16px; height: 16px; flex: none; }
</style>
</head>
<body>
  <section class="card card-front">
    <span class="brand-dot"></span>
    <h1 class="brand-name">Morvell Electric</h1>
  </section>

  <section class="card card-back">
    <div class="emboss-mark">
      <span class="emboss-ring"></span>
      <span class="emboss-name">Morvell Electric</span>
    </div>
    <div class="contact">
      <p class="person-name">Daniel Harper</p>
      <p class="person-role">Managing Director</p>
      <p class="address">738, Street line<br>goes here<br>58120, Region Name</p>
      <ul class="contact-list">
        <li>
          <svg viewBox="0 0 16 16" fill="none" stroke="#fff" stroke-width="1.6"><path d="M3 2h3l1 3-2 1.5a9 9 0 0 0 4.5 4.5L11 9l3 1v3a1 1 0 0 1-1 1A12 12 0 0 1 2 3a1 1 0 0 1 1-1z"/></svg>
          044-321 654 987
        </li>
        <li>
          <svg viewBox="0 0 16 16" fill="none" stroke="#fff" stroke-width="1.6"><rect x="1.5" y="3.5" width="13" height="9"/><path d="M1.5 3.5 8 9l6.5-5.5"/></svg>
          info@morvellmail.com
        </li>
        <li>
          <svg viewBox="0 0 16 16" fill="none" stroke="#fff" stroke-width="1.4"><circle cx="8" cy="8" r="6.5"/><ellipse cx="8" cy="8" rx="3" ry="6.5"/><path d="M1.5 8h13M2.5 5h11M2.5 11h11"/></svg>
          www.morvellsite.com
        </li>
      </ul>
    </div>
  </section>
</body>
</html>
```